Premium Nail Dip Powder Label Design

We need a label design for a 2 ounce jar in which we will be selling our new product line of dip powder to nail salons. For reference, please see competitors' products that are currently selling in the market. The label size is 16cm long by 2.5cm wide. We have a logo design that is attached - the "drop" should be in shiny gold (metallic). This label will wrap around the round jar and the first half will be the "front" and the second half will be the "back". Please see the attached writing that will be required for the second half, or "back" part of the label.

Target Market(s)

Retail Nail Salons in the US

Font styles to use
Sans Serif

Colors

Designer to choose colors to be used in the design.

Requirements
Must have
• "RVT" logo with the "drop" in shiny/metallic gold to match the shiny gold lid that we will have for it. The words "Premium Dip Powder". The size "2 oz". The wording for the second half, or "back" part of the label attached should be in black color with the size adjusted to fit the label size.
Nice to have
• different designs of fonts and sizes and colors for "Premium Dip Powder" which should be on the "front" of the label under our logo.

```html
<!DOCTYPE html>
<html lang="en">
<head>
<meta charset="utf-8">
<title>RVT Premium Dip Powder Label</title>
<link rel="stylesheet" href="https://fonts.googleapis.com/css2?family=Montserrat:wght@400;500;600&family=Playfair+Display:wght@400&display=swap">
<style>
  :root {
    --bg: #afc0d1;
    --label-top: #8c8c8c;
    --label-mid: #6f6f6f;
    --label-bottom: #3b3b3d;
    --gold: #c9a867;
    --type-light: #e9e9e9;
    --type-soft: #cfcfcf;
    --type-dark: #222222;
    --divider: rgba(255,255,255,0.18);
  }
  * { margin: 0; padding: 0; box-sizing: border-box; }
  html, body { width: 1200px; height: 857px; overflow: hidden; }
  body {
    background: var(--bg);
    font-family: "Montserrat", sans-serif;
    display: flex; align-items: center; justify-content: center;
  }
  .label {
    width: 1120px; height: 175px;
    display: flex;
    background: linear-gradient(180deg, var(--label-top) 0%, var(--label-mid) 45%, var(--label-bottom) 100%);
    box-shadow: 0 10px 30px rgba(40,55,75,0.25);
  }
  .label-front, .label-back { width: 50%; height: 100%; }
  .label-front {
    display: flex; flex-direction: column; align-items: center; justify-content: center;
    border-right: 1px dashed var(--divider);
  }
  .brand {
    display: flex; align-items: center; gap: 8px;
    font-family: "Montserrat", sans-serif; font-weight: 600;
    font-size: 34px; letter-spacing: 1px; color: var(--gold); line-height: 1;
  }
  .brand-dot { width: 10px; height: 10px; border-radius: 50%; background: var(--gold); }
  .premium {
    margin-top: 6px;
    font-size: 15px; font-weight: 400; letter-spacing: 7px;
    color: var(--type-soft); line-height: 1;
  }
  .product-name {
    margin-top: 6px;
    font-family: "Playfair Display", serif; font-size: 32px;
    letter-spacing: 5px; color: var(--type-light); line-height: 1;
  }
  .size {
    margin-top: 10px;
    font-size: 14px; color: var(--type-light); letter-spacing: 1px;
  }
  .label-back {
    padding: 22px 70px 0 70px;
    color: var(--type-dark);
    font-size: 10.5px; line-height: 1.45;
  }
  .warnings { list-style: none; margin-top: 3px; }
  .warnings li::before { content: "•"; margin-right: 6px; }
  .ingredients { margin-top: 8px; }
  .ingredients strong { font-weight: 600; }
  .maker { margin-top: 8px; font-style: italic; font-weight: 600; }
  .web { margin-top: 4px; }
</style>
</head>
<body>
  <section class="label">
    <div class="label-front">
      <div class="brand"><span class="brand-dot"></span>RVT</div>
      <div class="premium">PREMIUM</div>
      <div class="product-name">Dip Powder</div>
      <div class="size">2 oz</div>
    </div>
    <div class="label-back">
      <p>For Use By Nail Professionals Only.</p>
      <ul class="warnings">
        <li>CAUTION: KEEP OUT OF REACH OF CHILDREN</li>
        <li>Keep away from heat, humidity and sunlight</li>
        <li>Discontinue use if sensitivity or irritation occurs</li>
      </ul>
      <p class="ingredients"><strong>INGREDIENTS:</strong> Polyethylmethacrylate, Acrylates Copolymer, Benzoyl Peroxide and PEG-12 Dimethicone. May also contain various coloring agents and glitters.</p>
      <p class="maker">Manufactured Exclusively For: Blue Harbor Trading, Inc.</p>
      <p class="web">www.blueharbortrading.com</p>
    </div>
  </section>
</body>
</html>
```